Plakat-Design für Immobilienmakler und Baufinanzierer
Zielgruppe
Wir sind Immobilienmakler und Baufinanzierer und suchen ein hochwertiges Design, unsere Zielgruppe sind Kunden, die Ihr Haus verkaufen möchten. Für jeden erfolgreichen Verkauf spenden wir 5 % unserer Maklercourtage an einen Verein, den sich der Kunde aussuchen darf. Mit diesem Plakat wollen wir auf unsere Vereinsförderng aufmerksam machen und Vereine ansprechen.
Aufgabenstellung
Text: 'Wir spenden 5 % unserer Provision für Ihren Verein', 'Nur 1,99 % Maklercourtage', Logo, Kontaktdaten

```html
<!DOCTYPE html>
<html lang="de">
<head>
<meta charset="utf-8">
<title>Plakat Vereinsförderung – Halvern Immobilien</title>
<link href="https://fonts.googleapis.com/css2?family=Raleway:wght@300;400;600;700;800&display=swap" rel="stylesheet">
<style>
  :root{
    --stage:#e6e6e4;
    --paper:#f1efec;
    --teal:#1f5a5c;
    --stone:#a9a39b;
    --stone-dark:#8c857d;
    --tint:#d3dcdc;
  }
  *{margin:0;padding:0;box-sizing:border-box}
  html,body{width:1200px;height:1200px;overflow:hidden;background:var(--stage)}
  .poster{
    position:absolute;left:191px;top:30px;width:817px;height:1140px;
    background:var(--paper);overflow:hidden;
    font-family:"Raleway",sans-serif;
    box-shadow:0 6px 24px rgba(0,0,0,.12);
  }
  .poster__backdrop{
    position:absolute;inset:0;
    background:linear-gradient(160deg,var(--tint) 0%,var(--paper) 55%,var(--tint) 100%);
  }
  .brand{
    position:absolute;left:462px;top:88px;
    display:flex;align-items:center;gap:10px;
    font-size:22px;font-weight:600;letter-spacing:.08em;color:var(--teal);
    text-transform:uppercase;
  }
  .brand__mark{width:12px;height:12px;background:var(--teal)}
  .headline{
    position:absolute;left:51px;top:215px;
    text-transform:uppercase;line-height:68px;font-size:70px;letter-spacing:-.01em;
  }
  .headline__strong{display:block;font-weight:800;color:var(--teal)}
  .headline__light{display:block;font-weight:300;color:var(--stone)}
  .offer{
    position:absolute;left:51px;top:586px;
    font-size:22px;font-weight:700;color:var(--stone-dark);text-transform:uppercase;
  }
  .offer__rule{position:absolute;left:0;top:627px;width:419px;height:2px;background:var(--stone-dark)}
  .contact{
    position:absolute;left:51px;top:910px;font-style:normal;
    font-size:15.5px;line-height:19px;color:var(--teal);font-weight:400;
  }
  .contact p + p{margin-top:24px}
  .contact__name{font-weight:700}
</style>
</head>
<body>
<article class="poster">
  <div class="poster__backdrop" role="img" aria-label="Dezente geometrische Hintergrundflächen in hellem Graugrün"></div>

  <div class="brand"><span class="brand__mark"></span>Halvern Immobilien</div>

  <h1 class="headline">
    <span class="headline__strong">Wir spenden 5 %</span>
    <span class="headline__light">unserer Provision</span>
    <span class="headline__strong">für Ihren Verein</span>
  </h1>

  <p class="offer" style="top:560px">Nur 1,99 % Maklercourtage</p>
  <div class="offer__rule" style="top:600px"></div>

  <address class="contact" style="top:884px">
    <p><span class="contact__name">Halvern Immobilien</span><br>Lindenweg 12<br>47906 Kempen</p>
    <p>Tel: 02152 310 27 64<br>Mobil: 0171 428 905 36</p>
    <p>info@halvern-immobilien.de<br>www.halvern-immobilien.de</p>
  </address>
</article>
</body>
</html>
```